Online Cooking App Pitch Deck- (THIS IS NOT A FOOD BUSINESS OR FOOD SERVICE, NO FOOD PICTURES)

Project Goal:
Design a visually compelling pitch deck to be used for securing investment. Looking for the pitch deck to be about the design using shapes, colors, fonts and sizes. Must be creative yet simple and clean.
Color Palette:
https://huebrik.io/ff3800-ffe2db-fefefa-2d3e50-010b13

(We want most screens to use #FEFEFA)

This is the current pitch deck we need simplified and redesigned (USE TEXT IN THE VANDREL LINK TO SHOW IN YOUR DESIGN):

https://files.vandrel.net/slides/d/7QpLmZ2kTr84NwXaVbcY0-hoxjdEuvwKt/view?mode=share&uid=503921846170259384712&fmt=true&sd=true

Project is now guaranteed. Remember use the text in the vandrel link in powerpoint design. Use a little more color not just the logo color. Do not use any pictures of food this is not food related business. We care more about style and design of shapes, text, color fonts.

Target Market(s)

Investors (venture capitalists, angel investors) interested in innovative technology solutions within the food industry.

Font styles to use
Serif
Sans Serif

Requirements
Nice to have
• Simple, abstract background non distracting but complementary.
Should not have
• No pictures

```html
<!DOCTYPE html>
<html lang="en">
<head>
<meta charset="utf-8">
<title>Use of Funds – Panfold</title>
<link rel="stylesheet" href="https://fonts.googleapis.com/css2?family=Figtree:wght@400;500;600;700;800&display=swap">
<style>
  :root {
    --paper: #fefefa;
    --orange: #ff3800;
    --blue: #0070c0;
    --yellow: #ffc000;
    --ink: #010b13;
    --panel-left: #f1f1f2;
    --panel-right: #f7f7f7;
    --bar: #d9d9d9;
    --white: #ffffff;
  }
  * { box-sizing: border-box; margin: 0; padding: 0; }
  html, body { width: 1200px; height: 675px; overflow: hidden; background: var(--paper); }
  body { font-family: "Figtree", sans-serif; color: var(--ink); }
  .slide { position: relative; width: 1200px; height: 675px; overflow: hidden; background: var(--paper); }
  .decor { position: absolute; inset: 0; }
  .panel { position: absolute; top: 91px; height: 491px; border-radius: 38px; }
  .panel-left { left: 112px; width: 355px; background: var(--panel-left); }
  .panel-right { left: 469px; width: 574px; background: var(--panel-right); }
  .budget-row { position: absolute; left: 138px; width: 906px; height: 43px; }
  .amount-bar {
    position: absolute; left: 240px; top: 0; right: 0; height: 43px;
    background: var(--bar); border: 3px solid var(--white); border-radius: 22px;
    display: flex; align-items: center; justify-content: flex-end; padding-right: 14px;
    font-weight: 700; font-size: 19px; letter-spacing: 0.1px;
  }
  .category-pill {
    position: absolute; left: 0; top: 0; width: 312px; height: 43px;
    background: var(--orange); border: 3px solid var(--white); border-radius: 22px;
    display: flex; align-items: center; padding-left: 13px;
    color: var(--white); font-weight: 700; font-size: 14px;
  }
  .category-note {
    position: absolute; left: 157px; width: 290px;
    font-size: 18px; line-height: 21.5px; font-weight: 500; letter-spacing: -0.2px;
  }
  .total {
    position: absolute; right: 178px; top: 482px;
    color: var(--orange); font-weight: 800; font-size: 54px; letter-spacing: -0.5px;
  }
  .brand {
    position: absolute; right: 86px; top: 48px;
    color: var(--orange); font-weight: 800; font-size: 26px;
  }
  .tagline {
    position: absolute; left: 0; right: 0; top: 633px; text-align: center;
    font-weight: 700; font-size: 14px;
  }
  .tagline .accent { color: var(--orange); }
  .page-number { position: absolute; left: 1090px; top: 633px; font-size: 16px; font-weight: 500; }
</style>
</head>
<body>
<div class="slide">
  <svg class="decor" width="1200" height="675" viewBox="0 0 1200 675" aria-hidden="true">
    <circle cx="553" cy="-56" r="109" fill="none" stroke="var(--blue)" stroke-width="20"/>
    <circle cx="-84" cy="333" r="144" fill="none" stroke="var(--yellow)" stroke-width="21"/>
    <circle cx="1318" cy="600" r="166" fill="none" stroke="var(--orange)" stroke-width="23"/>
    <circle cx="1118" cy="760" r="172" fill="none" stroke="var(--orange)" stroke-width="23"/>
  </svg>

  <div class="brand">Panfold</div>

  <div class="panel panel-left"></div>
  <div class="panel panel-right"></div>

  <div class="budget-row" style="top:123px">
    <div class="amount-bar">2-yr runway $480K</div>
    <div class="category-pill">Development</div>
  </div>
  <p class="category-note" style="top:175px">Adding new features, ongoing maintenance, front-end design adjustments and implementation.</p>

  <div class="budget-row" style="top:276px">
    <div class="amount-bar">2-yr runway $480K</div>
    <div class="category-pill">Marketing &amp; Advertising</div>
  </div>
  <p class="category-note" style="top:331px">Adding new features, ongoing maintenance, front-end design adjustments and implementation.</p>

  <div class="budget-row" style="top:430px">
    <div class="amount-bar">2-yr runway $480K</div>
    <div class="category-pill">Operations</div>
  </div>
  <p class="category-note" style="top:488px">The day to day activities with the team and ongoing management of new relationships, etc.</p>

  <div class="total">$1M</div>

  <p class="tagline">Cook, <span class="accent">Learn,</span> Repeat</p>
  <p class="page-number">29</p>
</div>
</body>
</html>
```